Landing Page Design

We need a landing page template designed to support a clients Zintro Bidlink Campaigns. The client is called Merrow Plumbing and they install and repair hot water systems (only). They provide no other plumbing services.

We are really looking for a great looking landing page that is both engaging and functional.

Target Market(s)

Residential/Domestic market. Typically wives and partners who are typically home or run the household.

Industry/Entity Type

Plumbing

Number of Pages Required

1 page

Requirements
Must have
• Strong branding
Strong call to actions
Great and obvious looking buttons
Nice to have
• Smart use of colour
Should not have
• The design should not use old-style, serif fonts.

Do not include any plumbing images

```html
<!DOCTYPE html>
<html lang="en">
<head>
<meta charset="utf-8">
<title>Merrow Plumbing – Solar Hot Water Systems</title>
<link href="https://fonts.googleapis.com/css2?family=Questrial&family=Mulish:wght@400;700;800;900&display=swap" rel="stylesheet">
<style>
:root{
  --navy:#013a6f;
  --navy-deep:#002c57;
  --sky-top:#cfe6f6;
  --sky-bottom:#f2f8fc;
  --white:#ffffff;
  --orange:#f0662a;
  --orange-light:#f8874a;
  --red-orange:#e2441c;
  --text:#3b3b3b;
  --green-top:#b9e26a;
  --green-bottom:#5aaa12;
  --green-btn:#1f8a1c;
  --blue-btn:#1a87c9;
  --gold-btn:#d9a20a;
  --field-border:#9aa7b3;
}
*{box-sizing:border-box;margin:0;padding:0}
html,body{width:1200px;height:1093px;overflow:hidden}
body{position:relative;background:linear-gradient(180deg,var(--sky-top) 0,#e4f1fa 150px,var(--white) 420px,var(--white) 100%);font-family:"Questrial",sans-serif;color:var(--text)}
.abs{position:absolute}

.topbar{left:333px;top:0;width:734px;height:47px;background:var(--navy);border-radius:0 0 8px 8px;display:flex;align-items:center;justify-content:flex-end;gap:24px;padding-right:18px;color:var(--white);font-family:"Mulish",sans-serif;font-weight:700;font-size:16px}
.topbar .item{display:flex;align-items:center;gap:9px}
.topbar .phone{font-size:27px;font-weight:800;letter-spacing:.5px}

.brand{left:145px;top:60px;display:flex;align-items:center;gap:8px;font-family:"Mulish",sans-serif;font-weight:800;font-size:26px;color:var(--red-orange)}
.brand .dot{width:22px;height:22px;border-radius:50%;background:var(--orange)}

.hero-panel{left:132px;top:154px;width:936px;height:254px;background:var(--navy);border-radius:8px 8px 0 0}
.hero{left:143px;top:165px;width:616px;height:232px;border-radius:8px;background:linear-gradient(180deg,#b9c3cc 0,#c98b4a 30%,#f6c55a 55%,#fbe7a4 70%,#f4b24a 100%)}
.hero-title{right:27px;bottom:26px;text-align:right;color:var(--red-orange);font-size:37px;line-height:42px}
.hero-title b{font-family:"Mulish",sans-serif;font-weight:900;font-size:46px}

.features{left:792px;top:183px;list-style:none;color:var(--white);font-size:19px}
.features li{height:40.5px;display:flex;align-items:center;gap:20px}
.features svg{width:22px;height:22px}

.section-title{left:162px;top:442px;width:256px;height:39px;border-radius:8px;background:linear-gradient(180deg,var(--orange-light),var(--red-orange));color:var(--white);font-family:"Mulish",sans-serif;font-weight:800;font-size:18px;display:flex;align-items:center;padding-left:21px}
.photo{left:162px;top:512px;width:153px;height:253px;border-radius:8px;border:1px solid #c8c8c8;background:linear-gradient(90deg,#8e8e8e,#c9c9c9 60%,#e9dfd8)}
.copy{left:351px;top:513px;width:368px;font-family:Arial,sans-serif;font-size:11.2px;line-height:13.5px;color:#444}
.copy p{margin-bottom:13.5px}

.cta{top:853px;height:82px;border-radius:7px;display:flex;align-items:center;color:var(--white);font-family:"Mulish",sans-serif;box-shadow:0 1px 2px rgba(0,0,0,.35)}
.cta .icon{width:68px;height:100%;display:flex;align-items:center;justify-content:center;border-radius:7px 0 0 7px;background:rgba(0,0,0,.22)}
.cta .label{padding-left:14px;line-height:1}
.cta .small{font-size:17px;font-weight:400;display:block}
.cta .big{font-size:28px;font-weight:900;display:block;letter-spacing:.5px}
.cta-quote{left:165px;width:161px;background:linear-gradient(180deg,#5cbf2a,var(--green-btn) 55%,#0d5a10)}
.cta-site{left:343px;width:161px;background:linear-gradient(180deg,#5fc3ef,var(--blue-btn) 55%,#0b4f86)}
.cta-rebates{left:521px;width:212px;background:linear-gradient(180deg,#f2cf3a,var(--gold-btn) 55%,#8d6a04)}

.form-panel{left:759px;top:403px;width:309px;height:548px;background:var(--navy);border-radius:0 8px 8px 8px}
.offer{left:770px;top:404px;width:286px;height:80px;border-radius:7px;background:linear-gradient(180deg,var(--green-top),var(--green-bottom));color:var(--navy);font-size:15.5px;line-height:17.5px;padding:11px 0 0 9px}
.offer b{font-family:"Mulish",sans-serif;font-weight:800}
.enquiry{left:778px;top:497px;width:272px;color:var(--white);font-size:15px}
.enquiry label{display:block;height:18px;line-height:18px}
.enquiry .field{display:block;width:272px;height:30px;background:var(--white);border:2px solid var(--field-border);margin-bottom:6px}
.enquiry textarea.field{height:97px;resize:none}
.submit{left:877px;top:894px;width:172px;height:39px;border-radius:8px;border:none;background:linear-gradient(180deg,var(--orange-light),var(--red-orange));color:var(--white);font-family:"Mulish",sans-serif;font-weight:800;font-size:19px;display:flex;align-items:center;justify-content:center;gap:10px}

.footer{left:0;top:1001px;width:1200px;height:92px;background:var(--navy)}
.footer p{position:absolute;left:172px;top:13px;color:var(--white);font-family:Arial,sans-serif;font-size:12px}
</style>
</head>
<body>

<header class="topbar abs">
  <span class="item">
    <svg width="22" height="22" viewBox="0 0 22 22"><path d="M11 2 1 11h3v9h5v-6h4v6h5v-9h3z" fill="#f7931e"/></svg>
    Visit Our Website
  </span>
  <span class="item">
    <svg width="22" height="20" viewBox="0 0 22 20"><path d="M11 1 1 19h20z" fill="#f7931e"/><rect x="10" y="7" width="2" height="6" fill="#fff"/><rect x="10" y="15" width="2" height="2" fill="#fff"/></svg>
    Call NOW on <span class="phone">9471 3058</span>
  </span>
</header>

<div class="brand abs"><span class="dot"></span>Merrow Plumbing</div>

<div class="hero-panel abs"></div>
<div class="hero abs" role="img" aria-label="Sunset sky seen through falling water">
  <p class="hero-title abs">Harness the Energy<br>and <b>Save $$$!</b></p>
</div>

<ul class="features abs">
  <li><svg viewBox="0 0 22 22"><rect x="1" y="3" width="20" height="18" rx="2" fill="#5cb8f0"/><rect x="1" y="3" width="20" height="5" fill="#1d7fd0"/><g fill="#fff"><rect x="4" y="10" width="3" height="3"/><rect x="9.5" y="10" width="3" height="3"/><rect x="15" y="10" width="3" height="3"/><rect x="4" y="15" width="3" height="3"/><rect x="9.5" y="15" width="3" height="3"/><rect x="15" y="15" width="3" height="3"/></g></svg>Sydney 24Hours 7Days</li>
  <li><svg viewBox="0 0 22 22"><path d="M18 11a7 7 0 1 1-3-5.7" fill="none" stroke="#5cb8f0" stroke-width="3.5"/><path d="M12 2h7v7z" fill="#5cb8f0"/></svg>On Time</li>
  <li><svg viewBox="0 0 22 22"><rect x="1" y="1" width="20" height="20" rx="3" fill="#5cc22a"/><rect x="5" y="6" width="3" height="11" fill="#fff"/><rect x="10" y="9" width="7" height="2" fill="#fff"/><rect x="10" y="13" width="7" height="2" fill="#fff"/></svg>Professional Technicians</li>
  <li><svg viewBox="0 0 22 22"><path d="M3 2h16a2 2 0 0 1 2 2v10a2 2 0 0 1-2 2H10l-5 5v-5H3a2 2 0 0 1-2-2V4a2 2 0 0 1 2-2z" fill="#5cb8f0"/></svg>We Advise on Rebates</li>
  <li><svg viewBox="0 0 22 22"><path d="M11 1l3 7 7.5.6-5.7 5 1.8 7.4L11 17l-6.6 4 1.8-7.4L.5 8.6 8 8z" fill="#f7a52a"/></svg>Authorised Solvane Dealer</li>
</ul>

<h2 class="section-title abs">Solar Hot Water Systems</h2>
<div class="photo abs" role="img" aria-label="Person enjoying a warm shower"></div>
<div class="copy abs">
  <p>Lorem ipsum dolor sit amet, consectetur adipiscing elit. Fusce tristique suscipit augue in adipiscing. Sed aliquet dictum sem a rhoncus. In consequat consequat eros quis adipiscing. In risus dolor, fermentum non faucibus at, molestie quis dolor. Sed in sapien sit amet enim lacinia tempor eu ac erat. Donec luctus nibh a turpis mollis ultricies et id dui. In ac libero quis turpis ornare malesuada.</p>
  <p>Phasellus pellentesque pellentesque diam quis feugiat. Sed ipsum sapien, congue in ornare eu, consectetur vitae est. Donec rhoncus orci a est mollis laoreet. Nunc euismod rhoncus mi, ac fermentum ipsum commodo quis. Curabitur hendrerit, nibh sed molestie iaculis, nisi diam ultricies lorem, ac fringilla eros leo non nibh.</p>
  <p>Donec a ipsum non tortor tincidunt dignissim sed at nunc. Phasellus lectus nulla, fringilla non mattis in, tristique sed libero. Donec rhoncus tortor vel orci congue rhoncus. Phasellus at magna elit. Nam fringilla libero in eros lacinia adipiscing. Praesent auctor sodales facilisis. Nunc sit amet ante lacus, ac placerat massa. Fusce quis turpis at est semper</p>
</div>

<a class="cta cta-quote abs">
  <span class="icon"><svg width="40" height="44" viewBox="0 0 40 44"><rect x="4" y="2" width="24" height="32" fill="#7fd34a" transform="rotate(-12 16 18)"/><rect x="10" y="8" width="24" height="32" fill="#9fe36a" stroke="#0d5a10"/><g stroke="#0d5a10" stroke-width="2"><line x1="14" y1="16" x2="30" y2="16"/><line x1="14" y1="22" x2="30" y2="22"/><line x1="14" y1="28" x2="30" y2="28"/><line x1="14" y1="34" x2="26" y2="34"/></g></svg></span>
  <span class="label"><span class="small">Book a</span><span class="big">FREE</span><span class="small">Quote</span></span>
</a>
<a class="cta cta-site abs">
  <span class="icon"><svg width="44" height="40" viewBox="0 0 44 40"><path d="M22 3 3 20h5v17h28V20h5z" fill="none" stroke="#7fd0f5" stroke-width="3"/><rect x="17" y="24" width="10" height="13" fill="none" stroke="#7fd0f5" stroke-width="3"/></svg></span>
  <span class="label"><span class="small">Visit</span><span class="big">OUR</span><span class="small">Website</span></span>
</a>
<a class="cta cta-rebates abs">
  <span class="icon"><svg width="46" height="46" viewBox="0 0 46 46"><circle cx="23" cy="23" r="20" fill="#f5d431" stroke="#8d6a04" stroke-width="2"/><text x="23" y="33" text-anchor="middle" font-family="Mulish,sans-serif" font-weight="900" font-size="28" fill="#8d4a04">$</text></svg></span>
  <span class="label"><span class="small">Our</span><span class="big">REBATES</span><span class="small">Information</span></span>
</a>

<aside class="form-panel abs"></aside>
<div class="offer abs">Take advantage of this great offer.<br>Contact Us <b>NOW</b> on <b>9471 3058</b><br>or register your interest below</div>
<form class="enquiry abs">
  <label>Your First Name</label><input class="field" type="text">
  <label>Your Surname</label><input class="field" type="text">
  <label>Your Suburb</label><input class="field" type="text">
  <label>Best Contact Number</label><input class="field" type="tel">
  <label>Your Email Address</label><input class="field" type="email">
  <label>Enquiry / Comments</label><textarea class="field"></textarea>
</form>
<button class="submit abs" type="button">Enquire Now <svg width="7" height="12" viewBox="0 0 7 12"><path d="M1 1l5 5-5 5" fill="none" stroke="#fff" stroke-width="2"/></svg></button>

<footer class="footer abs"><p>© 2010 Merrow Plumbing. All Rights Reserved.</p></footer>

</body>
</html>
```